Dog walking/Pet Sitting company needs a brochure to hook high end apartment tenants

We are looking for a brochure design that we can bring to meetings with high-end apartment and hotel management that will explain who we are, what we do, and how we can help their tenants/guests. I would like it to reflect the same look and feel of our website, carried over to printed brochure. Wesbite is www.harborleashpetcare.com. I can provide the stock images from the website if needed. A bi-fold brochure is ideal, unless you feel the information would fit better on a tri-fold. My company colors are #5D4664 and #5BA046. I would like a more professional tone to it, rather than fun.

Target Market(s)

Demo Professional Females and Males ages 30-50 with pets

Industry/Entity Type

Pet sitting

Font styles to use
Sans Serif

Colors
6b449b
9bcb3c

Requirements
Must have
• the same look and feel as my website; explain who we are, what we do, how we can help; include services offered; Mention that we service Parsippany and surrounding towns. Mention 15 years in business.
Should not have
• do not list pricing on brochure (you can mention pricing is available on the website). No cartoonish feel.

```html
<!DOCTYPE html>
<html lang="en">
<head>
<meta charset="UTF-8">
<title>Harbor Leash Pet Care – Brochure Cover</title>
<link href="https://fonts.googleapis.com/css2?family=Montserrat:wght@400;500;700;800&display=swap" rel="stylesheet">
<style>
  :root {
    --stage: #2a2a2a;
    --paper: #ffffff;
    --brand-green: #5ba046;
    --brand-green-light: #74b45e;
    --brand-purple: #5d4664;
    --photo-light: #e8e2dc;
    --photo-warm: #c9a27e;
    --photo-dark: #6d5140;
  }
  * { box-sizing: border-box; margin: 0; padding: 0; }
  html, body { width: 1200px; height: 790px; overflow: hidden; }
  body {
    background: var(--stage);
    font-family: "Montserrat", sans-serif;
    display: flex;
    align-items: center;
    justify-content: center;
  }
  .cover {
    position: relative;
    width: 540px;
    height: 700px;
    background: var(--paper);
    overflow: hidden;
  }
  .cover-photo {
    position: absolute;
    inset: 0 0 auto 0;
    height: 470px;
    background:
      radial-gradient(ellipse at 55% 45%, var(--photo-warm) 0%, transparent 45%),
      radial-gradient(ellipse at 30% 40%, var(--photo-dark) 0%, transparent 40%),
      linear-gradient(180deg, var(--photo-light) 0%, #d9d2cb 100%);
  }
  .cover-band {
    position: absolute;
    left: 0; top: 0;
    width: 540px; height: 700px;
  }
  .brand-seal {
    position: absolute;
    left: 180px;
    top: 345px;
    width: 180px;
    height: 180px;
    border-radius: 50%;
    background: var(--paper);
    border: 6px solid var(--brand-green);
    display: flex;
    align-items: center;
    justify-content: center;
    text-align: center;
  }
  .brand-name {
    color: var(--brand-purple);
    font-weight: 700;
    font-size: 19px;
    line-height: 1.2;
    letter-spacing: 0.04em;
    text-transform: uppercase;
  }
  .cover-copy {
    position: absolute;
    left: 0; right: 0;
    top: 560px;
    text-align: center;
    color: var(--paper);
  }
  .tagline-lead {
    font-weight: 500;
    font-size: 22px;
    letter-spacing: 0.02em;
  }
  .tagline-main {
    font-weight: 800;
    font-size: 31px;
    margin-top: 4px;
  }
  .site-url {
    margin-top: 18px;
    font-size: 12px;
    letter-spacing: 0.28em;
    font-weight: 500;
  }
</style>
</head>
<body>
  <main class="cover">
    <div class="cover-photo" role="img" aria-label="Photo of a smiling woman hugging a fluffy Australian shepherd puppy"></div>

    <svg class="cover-band" viewBox="0 0 540 700" aria-hidden="true">
      <polygon points="0,470 540,405 540,700 0,700" fill="var(--brand-green)"/>
      <line x1="0" y1="470" x2="540" y2="405" stroke="var(--brand-purple)" stroke-width="5"/>
      <polygon points="510,700 540,670 540,700" fill="var(--brand-purple)"/>
    </svg>

    <div class="brand-seal">
      <span class="brand-name">Harbor Leash<br>Pet Care</span>
    </div>

    <div class="cover-copy">
      <p class="tagline-lead">Prioritize Your Family.</p>
      <p class="tagline-main">We'll Focus on Your Pets.</p>
      <p class="site-url">www.harborleashpetcare.com</p>
    </div>
  </main>
</body>
</html>
```